Start up business, dog breeder. Needs logo design and website.

I am a start up business looking for a logo design and a website. Ashmoor Creek Doodles is a breeder of goldendoodles and labradoodles for home and sport. We have a strong emphasis on hunting lines within our dogs and strive to breed healthy companions for the field and the home. These dogs are a cross between golden retrievers and poodles or Labrador retrievers and poodles (some multigenerational) and possess a strong hunt drive along with the desire to please. Some people can't tolerate shedding and dander, whether due to allergies or personal preference. That's one of the things that makes these dogs so versatile - they are all low to nonshedding and allergy friendly for most people. Combine that with the intelligence, loyalty, need to please, temperament and athletic ability, and you have an amazing pet. We are marketing to people that want a nonshedding pet, and also to people who want a hunting companion. It is important to reach both groups of buyers, but not to lean too much toward either one. (The dogs flush and retrieve for bird hunters - pheasant, dove, quail, duck, etc.) They are raised, bred and trained on our small farm in Golden Valley County, Beach North Dakota, where they have lots of room to run, exercise and train in the prairie lands. The term "adopt" a puppy is preferred over "buy" a puppy.

I have purchased the web address with a wordpress platform through net bramble.com. I started the website using one of their templates but wasn't pleased with it - need something far more professional than I'm capable of putting together. I will need help publishing the site and brief instructions on how to change and update when I have litters for adoption. I have quite a bit of content (text) and photos put together to give an idea of what we'd like it to say....feel free to edit away! I am no writer by any means, but it will share the business concept at least.

My "style" isn't really defined for a web design, but I can tell you what I like based on how I decorate my home: I love rustic mixed with dressy/contemporary, to offset all the rough edges, if that's any help. Think pallet wood walls with a crystal chandelier. I use lots of wood, plants, and repurpose old stuff for new uses. Natural, organic, texture.

I have a facebook page, but haven't done much with it yet. www.pagelinker.com/ashmoorcreekdoodles

I have a professional photographer coming to take photos of all my breeding stock next month, but I attached some snapshot photos to use as placeholders for the time being. Also attached of photo of my husband and I as owners and operators of Ashmoor Creek Doodles. Peter Lewis Haddon, and Rebecca Haddon

Target Market(s)

Allergy sufferers who need a low to non shedding dog
People looking to add a beautiful intelligent trainable house pet to their family
Bird and duck hunters who need a hunting companion

Industry/Entity Type

Marketing

Requirements
Must have
• 1. Adoption questionnaire for prospective buyers. Form details/fields attached. When the buyer clicks "submit" the form results should go to my email address
2. Coin nest option for deposits and final payments (we do not accept credit cards)
3. An "outdoorsy" feel. Natural. Organic.
4. We are marketing to people that want a nonshedding pet, and also to people who want a hunting companion. It is important to reach both groups of buyers, but not to lean too much toward either one.
Nice to have
• A rustic feel. Look at wentlockfieldpups.com
Some reference to our namesake/location. "Golden Valley" is the county we live in and is named so for the surrounding croplands. Think rolling fields of wheat, pheasants, wildlife, meadows, ponds, hunting.....
Should not have
• 1. Music
2. Nothing froo-froo or silly, nothing cartoonish
3. An example of what I don't like (very homemade looking, unprofessional, terrible layout, cartoony looking) http://www.quimbydoodles.net http://www.doodlesplorn.com

```html
<!DOCTYPE html>
<html lang="en">
<head>
<meta charset="utf-8">
<title>Ashmoor Creek Doodles</title>
<link href="https://fonts.googleapis.com/css2?family=Lato:wght@400;700&family=Open+Sans:wght@400;600;700&display=swap" rel="stylesheet">
<style>
:root{
  --teal:#1fa9c4;
  --teal-dark:#138aa2;
  --ink:#3a3a3a;
  --muted:#8a8a8a;
  --line:#e3e3e3;
  --soft:#f4f4f4;
  --red:#e0413a;
  --white:#ffffff;
  --footer:#f7f7f7;
}
*{box-sizing:border-box;margin:0;padding:0}
html,body{width:1200px;height:2660px;overflow:hidden;background:var(--white)}
body{font-family:"Open Sans",Arial,sans-serif;color:var(--ink);font-size:13px;line-height:1.6}
.page{width:1200px;height:2660px;position:relative}

/* header */
.site-header{height:88px;display:flex;align-items:center;justify-content:space-between;padding:0 60px 0 110px;border-bottom:1px solid var(--line)}
.brand{display:flex;align-items:center;gap:10px;font-family:"Lato",sans-serif;font-weight:700;font-size:20px;color:var(--teal-dark);line-height:1.05}
.brand-mark{width:30px;height:30px;border-radius:50%;background:var(--teal)}
.main-nav{display:flex;align-items:center;gap:4px}
.main-nav a{font-size:12px;font-weight:600;color:var(--ink);text-decoration:none;padding:10px 16px;letter-spacing:.5px}
.main-nav a.active{background:var(--teal);color:var(--white)}
.cart{margin-left:8px;width:22px;height:22px}

/* hero */
.hero{height:360px;position:relative;background:linear-gradient(180deg,#bcc8cf 0%,#a9b0a6 30%,#8a7656 55%,#6b5636 80%,#4e3d25 100%)}
.hero-arrow{position:absolute;top:160px;width:30px;height:30px;border-radius:50%;background:rgba(255,255,255,.85);display:flex;align-items:center;justify-content:center}
.hero-arrow.prev{left:10px}.hero-arrow.next{right:10px}

/* services */
.services{height:252px;display:flex;justify-content:center;gap:40px;padding-top:40px}
.service{width:230px;text-align:center}
.service-icon{width:64px;height:64px;border-radius:50%;border:2px solid var(--line);margin:0 auto 12px;display:flex;align-items:center;justify-content:center}
.service.featured .service-icon{background:var(--red);border-color:var(--red)}
.service h3{font-family:"Lato",sans-serif;font-size:16px;font-weight:400;margin-bottom:6px}
.service.featured h3{color:var(--red)}
.service p{font-size:11px;color:var(--muted);line-height:1.5}

/* gallery */
.gallery{display:flex;gap:18px;padding:20px 60px 0;height:360px;border-top:1px solid var(--line);padding-top:40px}
.gallery-menu{width:220px;border:1px solid var(--line)}
.gallery-menu h2{background:var(--teal);color:var(--white);font-family:"Lato",sans-serif;font-size:19px;font-weight:400;padding:12px 14px}
.gallery-menu li{list-style:none;font-size:11px;color:var(--muted);padding:9px 14px;border-bottom:1px solid var(--line)}
.gallery-menu li.current{color:var(--teal)}
.gallery-grid{flex:1;display:grid;grid-template-columns:repeat(4,1fr);gap:14px}
.photo{border-radius:2px}
.photo.tan{background:linear-gradient(135deg,#8c6a45,#c9a57a)}
.photo.grass{background:linear-gradient(135deg,#6d7d4a,#a88f62)}
.photo.dark{background:linear-gradient(135deg,#1e1e1e,#4a4a4a)}
.photo.tealwash{background:linear-gradient(135deg,#49b5c4,#9fd7d9)}
.photo.bw{background:linear-gradient(135deg,#2a2a2a,#9a9a9a)}

/* about */
.about{height:492px;padding:40px 110px 0}
.section-title{text-align:center;font-family:"Lato",sans-serif;font-size:32px;font-weight:400;letter-spacing:1px;color:var(--ink)}
.section-title span{color:var(--teal)}
.tabs{display:flex;justify-content:center;gap:4px;margin:16px 0 26px}
.tab{font-size:10px;padding:6px 22px;border:1px solid var(--line);color:var(--muted)}
.tab.active{background:var(--teal);color:var(--white);border-color:var(--teal)}
.about h3{color:var(--teal);font-family:"Lato",sans-serif;font-size:24px;font-weight:700;margin-bottom:10px}
.about p{font-size:11px;color:var(--muted);margin-bottom:8px}
.checklist{list-style:none;margin:12px 0 20px}
.checklist li{display:flex;align-items:center;gap:10px;font-size:12px;margin-bottom:8px}
.btn{display:inline-block;background:var(--teal);color:var(--white);font-size:11px;font-weight:700;padding:10px 22px;letter-spacing:.5px}

/* news + clients */
.band{height:408px;background:var(--soft);display:flex;gap:60px;padding:36px 110px 0}
.news{flex:1.15}
.band h2{font-family:"Lato",sans-serif;font-size:28px;font-weight:400;margin-bottom:18px}
.band h2 span{color:var(--teal)}
.news-item{display:flex;gap:14px;margin-bottom:20px}
.date{width:44px;height:50px;background:var(--ink);color:var(--white);text-align:center;font-weight:700;font-size:18px;line-height:1.2;padding-top:6px;flex:none}
.date small{display:block;font-size:9px;font-weight:400}
.news-item h4{font-size:13px;font-weight:600}
.news-item .meta{font-size:9px;color:var(--muted)}
.news-item p{font-size:10px;color:var(--muted);line-height:1.45}
.news-item p b{color:var(--teal)}
.clients{flex:1}
.quote{font-size:11px;color:var(--muted);font-style:italic;text-align:center;padding:0 20px}
.author{display:flex;justify-content:center;align-items:center;gap:8px;margin:12px 0 22px;font-size:10px}
.avatar{width:30px;height:30px;border-radius:50%;background:linear-gradient(135deg,#b7a79b,#6f6259)}
.newsletter{border:2px dashed var(--teal);background:var(--white);padding:16px 18px;width:300px;margin-left:40px}
.newsletter h4{color:var(--teal);font-size:14px;font-weight:600;margin-bottom:8px}
.newsletter .field{height:24px;border:1px solid var(--line);margin-bottom:8px}
.newsletter .send{display:inline-block;background:var(--teal);color:var(--white);font-size:10px;padding:4px 14px}

/* our clients */
.partners{height:388px;padding-top:40px;text-align:center}
.partners p.lead{font-size:11px;color:var(--muted);width:760px;margin:10px auto 34px}
.partner-row{display:flex;justify-content:center;gap:30px}
.partner{width:170px;height:100px;border:1px solid var(--line);display:flex;align-items:center;justify-content:center;gap:8px;font-family:"Lato",sans-serif;font-weight:700;font-size:13px;color:var(--teal)}
.partner i{width:14px;height:14px;border-radius:50%;background:var(--teal)}
.dots{margin-top:22px;display:flex;justify-content:center;gap:6px}
.dots b{width:8px;height:8px;border-radius:50%;background:var(--line)}
.dots b.on{background:var(--red)}

/* footer */
.site-footer{height:292px;background:var(--footer);border-top:1px solid var(--line);padding:24px 60px 0;display:flex;gap:40px;position:relative}
.footer-info{flex:1}
.site-footer h5{font-size:11px;font-weight:700;margin-bottom:10px;text-transform:uppercase}
.info-item{display:flex;gap:10px;margin-bottom:10px}
.thumb{width:42px;height:34px;background:linear-gradient(135deg,#c9b28f,#7d6a4d);flex:none}
.info-item p{font-size:9.5px;color:var(--muted);line-height:1.4}
.info-item p b{color:var(--ink)}
.footer-gallery{width:280px}
.footer-grid{display:grid;grid-template-columns:repeat(3,1fr);gap:6px}
.footer-grid div{height:46px}
.footer-bar{position:absolute;left:0;right:0;bottom:0;height:40px;border-top:1px solid var(--line);display:flex;align-items:center;justify-content:space-between;padding:0 60px;font-size:10px;color:var(--muted)}
.pay{display:flex;gap:6px}
.pay span{width:34px;height:20px;border-radius:2px;background:#d4d4d4}
</style>
</head>
<body>
<div class="page">

<header class="site-header">
  <div class="brand"><span class="brand-mark"></span><span>Ashmoor Creek<br>Doodles</span></div>
  <nav class="main-nav">
    <a class="active">HOME</a><a>DAMS</a><a>SIRES</a><a>PUPPIES</a><a>ADOPTION</a><a>CONTACT US</a>
    <svg class="cart" viewBox="0 0 24 24" fill="none" stroke="#3a3a3a" stroke-width="2"><path d="M3 4h3l2 11h11l2-8H7"/><circle cx="10" cy="19" r="1.5"/><circle cx="17" cy="19" r="1.5"/></svg>
  </nav>
</header>

<section class="hero" role="img" aria-label="Doodle sitting among tall dry prairie grass beside a pond">
  <span class="hero-arrow prev"><svg width="12" height="12" viewBox="0 0 12 12"><path d="M8 1 3 6l5 5" stroke="#3a3a3a" stroke-width="2" fill="none"/></svg></span>
  <span class="hero-arrow next"><svg width="12" height="12" viewBox="0 0 12 12"><path d="m4 1 5 5-5 5" stroke="#3a3a3a" stroke-width="2" fill="none"/></svg></span>
</section>

<section class="services">
  <div class="service"><div class="service-icon"><svg width="28" height="20" viewBox="0 0 28 20"><rect x="2" y="8" width="24" height="9" rx="4" fill="#3a3a3a"/></svg></div><h3>Dog Beds</h3><p>Cosy beds sized for every pup, washable covers and soft filling for restful nights.</p></div>
  <div class="service"><div class="service-icon"><svg width="24" height="24" viewBox="0 0 24 24"><circle cx="12" cy="12" r="9" fill="none" stroke="#3a3a3a" stroke-width="2"/><path d="M12 7v10M7 12h10" stroke="#3a3a3a" stroke-width="2"/></svg></div><h3>Puppy Care</h3><p>Health checks, early training and socialising before puppies head to their homes.</p></div>
  <div class="service featured"><div class="service-icon"><svg width="26" height="20" viewBox="0 0 26 20"><path d="M3 8h20l-3 10H6z" fill="#fff"/></svg></div><h3>Dog Food</h3><p>Quality nutrition plans that keep growing dogs strong for the field and the home.</p></div>
  <div class="service"><div class="service-icon"><svg width="26" height="24" viewBox="0 0 26 24"><path d="M3 12 13 3l10 9v10H3z" fill="none" stroke="#3a3a3a" stroke-width="2"/></svg></div><h3>Bed Dog Shelter</h3><p>Warm shelters with room to rest, built for long prairie winters and hot summers.</p></div>
</section>

<section class="gallery">
  <aside class="gallery-menu">
    <h2>Photo Gallery</h2>
    <ul>
      <li class="current">All Photos</li><li>Goldendoodles</li><li>Beagle</li><li>Labradoodles</li><li>English Shepherd</li><li>Dog Breeders</li>
    </ul>
  </aside>
  <div class="gallery-grid">
    <div class="photo tan" role="img" aria-label="Golden puppy portrait"></div>
    <div class="photo grass" role="img" aria-label="Doodle standing in a field"></div>
    <div class="photo tealwash" role="img" aria-label="Puppy photo with teal overlay"></div>
    <div class="photo dark" role="img" aria-label="Black doodle sitting"></div>
    <div class="photo tealwash" role="img" aria-label="Doodle outdoors with teal overlay"></div>
    <div class="photo grass" role="img" aria-label="Curly doodle on grass"></div>
    <div class="photo bw" role="img" aria-label="Black and white dog portrait"></div>
    <div class="photo dark" role="img" aria-label="Black puppy lying down"></div>
  </div>
</section>

<section class="about">
  <h2 class="section-title">ABOUT <span>OUR</span> PUPPIES</h2>
  <div class="tabs"><span class="tab active">ABOUT THE DOGS</span><span class="tab">ABOUT THE BREED</span><span class="tab">ABOUT THE FARM</span></div>
  <h3>Puppies Discription</h3>
  <p>Our doodles are raised on a small prairie farm with plenty of room to run, train and explore. Each litter is bred for health, temperament and a strong drive to please, making them wonderful companions whether at home or out in the field with bird hunters chasing pheasant, dove, quail and duck.</p>
  <p>These dogs are low to non shedding and allergy friendly for most people. Combine that with intelligence, loyalty, temperament and athletic ability, and you have an amazing family pet and a dependable hunting partner in one.</p>
  <ul class="checklist">
    <li><svg width="14" height="14" viewBox="0 0 14 14"><path d="m2 7 3 3 7-7" stroke="#1fa9c4" stroke-width="2.4" fill="none"/></svg>Low to non shedding coats suited to allergy sufferers and tidy homes.</li>
    <li><svg width="14" height="14" viewBox="0 0 14 14"><path d="m2 7 3 3 7-7" stroke="#1fa9c4" stroke-width="2.4" fill="none"/></svg>Strong hunting lines that flush and retrieve for upland and waterfowl.</li>
    <li><svg width="14" height="14" viewBox="0 0 14 14"><path d="m2 7 3 3 7-7" stroke="#1fa9c4" stroke-width="2.4" fill="none"/></svg>Early training and socialising on the farm before adoption day.</li>
    <li><svg width="14" height="14" viewBox="0 0 14 14"><path d="m2 7 3 3 7-7" stroke="#1fa9c4" stroke-width="2.4" fill="none"/></svg>Health tested parents and ongoing support for every family.</li>
  </ul>
  <span class="btn">READ MORE</span>
</section>

<section class="band">
  <div class="news">
    <h2>Latest <span>News</span></h2>
    <article class="news-item"><div class="date">21<small>MAR</small></div><div><h4>Spring Litter Now Taking Deposits</h4><div class="meta">Posted by admin · 4 Comments</div><p>Our spring litter of goldendoodles has arrived healthy and strong. Families on the waiting list can now place a deposit and start the adoption questionnaire. <b>Read more</b></p></div></article>
    <article class="news-item"><div class="date">15<small>MAR</small></div><div><h4>First Days Of Field Training</h4><div class="meta">Posted by admin · 2 Comments</div><p>The older pups took their first walks through the prairie grass this week, learning to follow scent and return on call with real enthusiasm. <b>Read more</b></p></div></article>
    <article class="news-item"><div class="date">02<small>MAR</small></div><div><h4>Caring For A Non Shedding Coat</h4><div class="meta">Posted by admin · 6 Comments</div><p>A few simple grooming habits keep a doodle coat soft, clean and tangle free, whether your dog spends its days on the couch or in a duck blind. <b>Read more</b></p></div></article>
  </div>
  <div class="clients">
    <h2>Happy <span>Clients</span></h2>
    <p class="quote">“Our pup settled into family life right away and is gentle with the kids, yet comes alive the moment we head out to the field. We could not have asked for a better companion.”</p>
    <div class="author"><span class="avatar" role="img" aria-label="Client portrait"></span><span><b>Client Name</b><br>Happy Owner</span></div>
    <div class="newsletter">
      <h4>Subscribe to Our Newsletter</h4>
      <div class="field"></div><div class="field"></div>
      <span class="send">SEND</span>
    </div>
  </div>
</section>

<section class="partners">
  <h2 class="section-title"><span>Our</span> Clients</h2>
  <p class="lead">Families and hunters across the region have welcomed our doodles into their homes and blinds. We are proud of every match and keep in touch as each dog grows into a loyal companion and working partner.</p>
  <div class="partner-row">
    <div class="partner"><i></i>YOUR LOGO HERE</div>
    <div class="partner"><i></i>YOUR LOGO HERE</div>
    <div class="partner"><i></i>YOUR LOGO HERE</div>
    <div class="partner"><i></i>YOUR LOGO HERE</div>
    <div class="partner"><i></i>YOUR LOGO HERE</div>
  </div>
  <div class="dots"><b class="on"></b><b></b><b></b></div>
</section>

<footer class="site-footer">
  <div class="footer-info">
    <h5>Potential Client Information</h5>
    <div class="info-item"><div class="thumb" role="img" aria-label="Puppy thumbnail"></div><p><b>Please add any further information you wish to consider in placing one of our doodles with you.</b><br>Tell us about your home, your yard, other pets and whether you hunt, so we can match the right pup.</p></div>
    <div class="info-item"><div class="thumb" role="img" aria-label="Puppy thumbnail"></div><p><b>Please add any further information you wish to consider in placing one of our doodles with you.</b><br>Let us know about allergies in the household and how much time you spend outdoors each week.</p></div>
    <div class="info-item"><div class="thumb" role="img" aria-label="Puppy thumbnail"></div><p><b>Please add any further information you wish to consider in placing one of our doodles with you.</b><br>Share any training goals, from quiet house manners to flushing and retrieving birds.</p></div>
  </div>
  <div class="footer-gallery">
    <h5>Gallery on Pixtrail</h5>
    <div class="footer-grid">
      <div class="photo tan" role="img" aria-label="Dog photo"></div><div class="photo grass" role="img" aria-label="Dog photo"></div><div class="photo dark" role="img" aria-label="Dog photo"></div>
      <div class="photo bw" role="img" aria-label="Dog photo"></div><div class="photo tan" role="img" aria-label="Dog photo"></div><div class="photo grass" role="img" aria-label="Dog photo"></div>
      <div class="photo dark" role="img" aria-label="Dog photo"></div><div class="photo tealwash" role="img" aria-label="Dog photo"></div><div class="photo tan" role="img" aria-label="Dog photo"></div>
    </div>
  </div>
  <div class="footer-bar">
    <span>HOME | DAMS | SIRES | PUPPIES | ADOPTION | CONTACT US · Ashmoor Creek Doodles</span>
    <div class="pay"><span></span><span></span><span></span><span></span><span></span></div>
  </div>
</footer>

</div>
</body>
</html>
```